Redesign of an educational Eye website for Medical Students and Healthcare professionals

www.corvantisportal.com is an educational resource, illustrated using high quality 3D animations, for undergraduate medical students and healthcare professionals to learn about the anatomy of the human eye and associated common eye disorders.

The website was originally developed (using a Joomla template) a couple of years ago and we now want to update the brand and design of the site. Example content and animations can be found at https://www.corvantisportal.com/overview or https://www.corvantisportal.com/ocular-anatomy/orbital-anatomy

We would like a new logo and home page design (to include new colour palette, fonts and updated overall design).

The attached PowerPoint contains an example layout of the revised components we want to appear on the new Home page. We plan to have a hero panel at the top of page playing a short video of some of the animations. Similar to how this site works (www.zembri.uk.com).

We want the new site to feel Professional, Modern and Clean and simple.

Target Market(s)

Undergraduate medical students and Healthcare Professionals

Industry/Entity Type

Medical

Logo Text

Corvantis Portal

Number of Pages Required

1 page

Font styles to use
Sans Serif

Colors

Designer to choose colors to be used in the design.

```html
<!DOCTYPE html>
<html lang="en">
<head>
<meta charset="utf-8">
<title>Corvantis Portal – Learn faster and smarter</title>
<link href="https://fonts.googleapis.com/css2?family=Roboto:wght@300;400;500;700&display=swap" rel="stylesheet">
<style>
  :root{
    --navy:#0d3560;
    --navy-deep:#0a2a4d;
    --blue:#2e8fd1;
    --blue-light:#4aa3de;
    --ink:#2b2f36;
    --muted:#5c636d;
    --page:#ffffff;
    --soft:#f3f4f6;
    --why-bg:#e8eef6;
    --rule:#9ec3e6;
    --footer:#e4e5e7;
    --badge:#dcdfe3;
  }
  *{box-sizing:border-box;margin:0;padding:0}
  html,body{width:1200px;height:4712px;overflow:hidden}
  body{font-family:"Roboto",Arial,sans-serif;color:var(--ink);background:var(--page);position:relative}
  section,header,footer{position:relative;width:1200px;overflow:hidden}

  /* Hero */
  .hero{height:710px;color:#fff}
  .hero-media{position:absolute;inset:0;background:linear-gradient(180deg,#6e5444 0%,#4e3a2f 50%,#2c221c 100%)}
  .hero-shade{position:absolute;inset:0;background:linear-gradient(180deg,rgba(0,0,0,0) 0%,rgba(0,0,0,.3) 60%,rgba(0,0,0,.4) 100%)}
  .brand{position:absolute;left:78px;top:28px;display:flex;align-items:center;gap:10px;font-size:22px;font-weight:400;color:#fff}
  .brand-mark{width:14px;height:14px;border-radius:50%;background:#fff}
  .sign-in{position:absolute;right:60px;top:36px;font-size:14px;letter-spacing:.5px;color:#fff}
  .hero-title{position:absolute;top:352px;width:100%;text-align:center;font-size:44px;font-weight:500}
  .hero-lead{position:absolute;top:418px;left:217px;width:766px;text-align:center;font-size:17px;line-height:28px;font-weight:300}
  .hero-actions{position:absolute;top:568px;width:100%;display:flex;justify-content:center;gap:30px}
  .btn{display:inline-flex;align-items:center;justify-content:center;height:48px;font-size:16px;color:#fff;text-decoration:none}
  .btn-navy{background:var(--navy);width:238px}
  .btn-blue{background:var(--blue);width:238px}

  /* Trusted */
  .trusted{height:273px;background:var(--page)}
  .trusted h2{position:absolute;top:30px;width:100%;text-align:center;font-size:15px;font-weight:400;letter-spacing:.5px;color:var(--muted)}
  .badges{position:absolute;top:100px;left:0;width:100%;display:flex;justify-content:space-around;padding:0 90px}
  .badge{width:150px;height:90px;background:var(--badge);border-radius:4px}

  /* Why */
  .why{height:644px;background:var(--why-bg)}
  .why-media{position:absolute;left:0;top:0;width:580px;height:644px;background:linear-gradient(90deg,#8a231b 0%,#b23a2e 45%,#e6e6e6 80%,#f5f5f5 100%)}
  .why-body{position:absolute;left:612px;top:50px;width:520px}
  .why-body h2{font-size:33px;font-weight:300;color:#3b3f46;margin-bottom:46px}
  .why-body h3{font-size:31px;font-weight:300;color:var(--blue);margin-bottom:22px}
  .why-body p{font-size:14px;color:var(--ink);margin-bottom:8px}
  .why-body ul{list-style:none;margin-bottom:70px}
  .why-body li{font-size:14px;line-height:24px;color:var(--ink);padding-left:16px;position:relative}
  .why-body li::before{content:"›";position:absolute;left:2px;color:var(--blue)}

  /* Modules */
  .modules{height:641px;background:var(--soft)}
  .section-title{position:absolute;width:100%;text-align:center;font-size:34px;font-weight:300;color:#3b3f46}
  .modules .section-title{top:48px}
  .module-grid{position:absolute;top:145px;left:75px;display:flex;gap:27px}
  .module{width:333px;height:405px;background:#fff;box-shadow:0 1px 4px rgba(0,0,0,.12)}
  .module-media{height:183px}
  .m1{background:linear-gradient(180deg,#4a82bd 0%,#2d5f9a 100%)}
  .m2{background:linear-gradient(180deg,#b8675b 0%,#9a4a42 100%)}
  .m3{background:linear-gradient(160deg,#e9c8b2 0%,#c9987c 100%)}
  .module-body{padding:24px 20px}
  .module h3{font-size:19px;font-weight:400;color:#2b2f36;margin-bottom:16px}
  .module p{font-size:13px;line-height:21px;color:var(--muted);height:72px}
  .module a{font-size:13px;color:var(--blue);text-decoration:none}

  .rule{position:absolute;left:56px;width:1088px;height:2px;background:var(--rule)}

  /* Team */
  .team{height:440px;background:var(--soft)}
  .team .section-title{top:55px}
  .team-grid{position:absolute;top:148px;left:75px;display:flex;gap:27px}
  .member{width:333px;height:223px;background:#eaeff4;position:relative;box-shadow:0 1px 3px rgba(0,0,0,.08)}
  .member-info{position:absolute;left:16px;top:58px}
  .member h3{font-size:16px;font-weight:500;color:var(--blue);margin-bottom:8px}
  .member p{font-size:11px;color:var(--ink)}
  .member-photo{position:absolute;right:0;bottom:0;width:165px;height:223px;background:linear-gradient(180deg,#e3e7ec 0%,#c3cad3 55%,#48505c 100%)}

  /* Testimonial */
  .voices{height:559px;background:#fff}
  .voices .section-title{top:50px;font-size:30px}
  .quote-mark{position:absolute;left:166px;top:108px;font-size:110px;line-height:1;color:var(--blue-light);font-family:Georgia,serif}
  .quote{position:absolute;left:240px;top:140px;width:720px;font-size:15px;line-height:29px;color:var(--muted);text-align:center}
  .quote-name{position:absolute;top:345px;width:100%;text-align:center;font-size:14px;font-weight:500;color:var(--blue)}
  .quote-role{position:absolute;top:373px;width:100%;text-align:center;font-size:13px;font-weight:700;color:var(--ink)}
  .dots{position:absolute;top:430px;width:100%;display:flex;justify-content:center;gap:12px}
  .dot{width:13px;height:13px;border-radius:50%;background:#d4d6d9}
  .dot.active{background:#9a9ea5}

  /* Trial */
  .trial{height:462px;color:#fff}
  .trial-media{position:absolute;inset:0;background:linear-gradient(180deg,#2f8ccf 0%,#1d6cae 100%)}
  .trial h2{position:absolute;top:105px;width:100%;text-align:center;font-size:40px;font-weight:700;color:var(--navy-deep)}
  .trial-sub{position:absolute;top:162px;width:100%;text-align:center;font-size:40px;font-weight:300;color:#fff}
  .trial-sub strong{font-weight:700}
  .trial-note{position:absolute;top:228px;width:100%;text-align:center;font-size:14px}
  .trial .btn{position:absolute;left:480px;top:300px;width:240px;height:46px;background:var(--navy-deep);font-size:15px}

  /* Charity */
  .charity{height:465px;background:var(--navy)}
  .charity-media{position:absolute;left:0;top:0;width:600px;height:465px;background:linear-gradient(110deg,#3a2a24 0%,#6b4c3c 40%,#4c6e8e 75%,#1f4a78 100%)}
  .charity-fade{position:absolute;left:440px;top:0;width:200px;height:465px;background:linear-gradient(90deg,rgba(13,53,96,0) 0%,var(--navy) 100%)}
  .charity-body{position:absolute;left:676px;top:55px;width:440px;color:#fff}
  .charity-body h2{font-size:32px;font-weight:500;line-height:46px;margin-bottom:26px;width:420px}
  .charity-body p{font-size:15px;line-height:26px;font-weight:300}

  /* Newsletter */
  .newsletter{height:367px;background:linear-gradient(180deg,#1f4d7c 0%,#163e68 100%);color:#fff}
  .newsletter h2{position:absolute;top:38px;width:100%;text-align:center;font-size:26px;font-weight:500}
  .newsletter p{position:absolute;top:83px;width:100%;text-align:center;font-size:13px}
  .signup{position:absolute;top:138px;left:252px;display:flex;gap:28px}
  .signup input{width:425px;height:44px;border:0;padding:0 16px;font-family:inherit;font-size:14px;color:#555}
  .signup button{width:153px;height:44px;border:0;background:var(--blue);color:#fff;font-family:inherit;font-size:16px}

  /* Footer */
  .site-footer{height:151px;background:var(--footer)}
  .foot-nav a{position:absolute;top:40px;font-size:13px;color:#333;text-decoration:none}
  .social{position:absolute;right:130px;top:30px;display:flex;gap:22px}
  .social span{width:30px;height:30px;border-radius:50%;background:var(--navy)}
  .foot-rule{position:absolute;left:60px;right:60px;top:95px;height:1px;background:#c6c8cb}
  .foot-legal{position:absolute;left:75px;top:115px;font-size:11px;color:#333;display:flex;gap:26px}
  .copyright{position:absolute;right:60px;top:115px;font-size:11px;color:#333}
</style>
</head>
<body>

<header class="hero">
  <div class="hero-media" role="img" aria-label="Close-up photograph of a man's eyes, hero video still"></div>
  <div class="hero-shade"></div>
  <div class="brand"><span class="brand-mark"></span>Corvantis Portal</div>
  <a class="sign-in">SIGN IN</a>
  <h1 class="hero-title">Learn faster and smarter</h1>
  <p class="hero-lead">Corvantis Portal helps undergraduates and healthcare professionals to learn or update their knowledge about the clinically relevant anatomy, ophthalmic examination techniques and common eye disorders of the human eye.</p>
  <div class="hero-actions">
    <a class="btn btn-navy">Undergraduates ›</a>
    <a class="btn btn-blue">Healthcare Professionals ›</a>
  </div>
</header>

<section class="trusted">
  <h2>TRUSTED ACROSS THE WORLD</h2>
  <div class="badges">
    <div class="badge" role="img" aria-label="Partner badge"></div>
    <div class="badge" role="img" aria-label="Partner badge"></div>
    <div class="badge" role="img" aria-label="Partner badge"></div>
    <div class="badge" role="img" aria-label="Partner badge"></div>
  </div>
</section>

<section class="why">
  <div class="why-media" role="img" aria-label="3D cross-section illustration of the human eye"></div>
  <div class="why-body">
    <h2>Why Corvantis Portal?</h2>
    <h3>Credible</h3>
    <p>Written and illustrated by experienced Consultant Ophthalmologists</p>
    <ul>
      <li>Concise text and structured content</li>
      <li>Practical clinical emphasis</li>
      <li>Each core topic distilled to the essential learning points</li>
    </ul>
    <h3>Visual</h3>
    <p>Key concepts brought to life using stunning 3D animations</p>
    <ul>
      <li>Helps you build a comprehensive feedback strategy</li>
      <li>Gives your whole organisation real-time, valuable insights</li>
      <li>Grows with your increasing need</li>
    </ul>
  </div>
</section>

<section class="modules">
  <h2 class="section-title">Training Modules</h2>
  <div class="module-grid">
    <article class="module">
      <div class="module-media m1" role="img" aria-label="3D illustration of the eyeball anatomy"></div>
      <div class="module-body">
        <h3>Core Principles</h3>
        <p>Covers clinically relevant anatomy, fundamental topics and examination techniques in Ophthalmology.</p>
        <a>Learn more</a>
      </div>
    </article>
    <article class="module">
      <div class="module-media m2" role="img" aria-label="Photograph of a red, irritated eye"></div>
      <div class="module-body">
        <h3>Ophthalmology in Practice</h3>
        <p>Deals with common eye disorders regularly encountered by healthcare professionals.</p>
        <a>Learn more</a>
      </div>
    </article>
    <article class="module">
      <div class="module-media m3" role="img" aria-label="Photograph of an eyelid being examined"></div>
      <div class="module-body">
        <h3>Visual acuity examination</h3>
        <p>The term vision includes several components including central vision.</p>
        <a>Learn more</a>
      </div>
    </article>
  </div>
  <div class="rule" style="top:639px"></div>
</section>

<section class="team">
  <h2 class="section-title">Meet the team</h2>
  <div class="team-grid">
    <article class="member">
      <div class="member-info"><h3>Tomas Hallgren</h3><p>Consultant Ophthalmologist</p></div>
      <div class="member-photo" role="img" aria-label="Portrait of team member"></div>
    </article>
    <article class="member">
      <div class="member-info"><h3>Rafael Ostin</h3><p>Consultant Ophthalmologist</p></div>
      <div class="member-photo" role="img" aria-label="Portrait of team member"></div>
    </article>
    <article class="member">
      <div class="member-info"><h3>Owen Brackley</h3><p>CTO</p></div>
      <div class="member-photo" role="img" aria-label="Portrait of team member"></div>
    </article>
  </div>
  <div class="rule" style="top:438px"></div>
</section>

<section class="voices">
  <h2 class="section-title">What people are saying about Corvantis Portal?</h2>
  <div class="quote-mark">“</div>
  <p class="quote">What sets this website apart are the superb 3D animations which enhance the accompanying text more effectively than clinical videos or photographs. I would whole heartedly recommend it to medical students, optometrists, GP's, casualty doctors and ophthalmic nurse practitioners, both as an introduction to ophthalmology, but also to refresh their knowledge of core ophthalmic examination techniques and conditions.</p>
  <div class="quote-name">Westmoor Deanery RTC</div>
  <div class="quote-role">Consultant Ophthalmologist and Head of the School of Ophthalmology</div>
  <div class="dots"><span class="dot active"></span><span class="dot"></span><span class="dot"></span></div>
</section>

<section class="trial">
  <div class="trial-media" role="img" aria-label="Blue close-up photograph of an iris"></div>
  <h2>Want to try Corvantis Portal for free?</h2>
  <div class="trial-sub">It's completely <strong>FREE</strong> for <strong>7 days</strong></div>
  <div class="trial-note">No credit card details required</div>
  <a class="btn">Join Now</a>
</section>

<section class="charity">
  <div class="charity-media" role="img" aria-label="Photograph of a child having an eye examination"></div>
  <div class="charity-fade"></div>
  <div class="charity-body">
    <h2>We give 10% of our profits to charity</h2>
    <p>We believe it is important to give something back so from 2018 we will donate 10% of every subscription to a selected charity somewhere in the world which works to help prevent sight loss and treat eye diseases.</p>
  </div>
</section>

<section class="newsletter">
  <h2>Join our Newsletter</h2>
  <p>Please enter your e-mail address below and then click the Sign Up button.</p>
  <form class="signup">
    <input type="email" placeholder="Email address...">
    <button type="button">Sign Up</button>
  </form>
</section>

<footer class="site-footer">
  <nav class="foot-nav">
    <a style="left:163px">HOME</a>
    <a style="left:289px">ABOUT</a>
    <a style="left:414px">CHAPTERS</a>
    <a style="left:575px">FAQ</a>
    <a style="left:681px">CONTACT</a>
  </nav>
  <div class="social"><span></span><span></span><span></span></div>
  <div class="foot-rule"></div>
  <div class="foot-legal"><span>Terms of Use</span><span>Privacy and Cookies</span></div>
  <div class="copyright">Copyright © 2018. Corvantis Portal</div>
</footer>

</body>
</html>
```